Delcourt Realty Business Cards

Design business card

Target Market(s)

High-End Buyer of Real Estate over $1 million dollars

Industry/Entity Type

Realtor

Contact Information for Business Card

Lena Delcourt R(S) LIC.# 41972
Cell 555 246-1938
Email Lena@Delcourt.example
Website IsleFreshHomes.example

Also Need Cards for:

Hank Delcourt R(B) LIC# 69418
C 555 613-7052
E Hank@Delcourt.example
W IsleFreshHomes.example

Colors

Designer to choose colors to be used in the design.

Requirements
Must have
• Address on back:
• 287 Pohaku Cir. , Wailea HI 96753
• Logo on back
Nice to have
• I would like the phone numbers and email address to be big so people can read it easily
Should not have
• Very small print Except For: address (287 Pohaku Cir. Wailea HI 96753)

```html
<!DOCTYPE html>
<html lang="en">
<head>
<meta charset="utf-8">
<title>Delcourt Realty Business Cards</title>
<link href="https://fonts.googleapis.com/css2?family=Cormorant+Garamond:wght@400;500;600;700&display=swap" rel="stylesheet">
<style>
  :root {
    --bg: #ececec;
    --charcoal: #2f2f31;
    --charcoal-deep: #262628;
    --stone: #dfded9;
    --paper: #ffffff;
    --ink: #2b2b2d;
    --silver: #c9c9c9;
    --photo-light: #f4f4f4;
    --photo-mid: #d9d9d9;
  }
  * { box-sizing: border-box; margin: 0; padding: 0; }
  html, body { width: 1200px; height: 1200px; overflow: hidden; }
  body {
    background: var(--bg);
    font-family: "Cormorant Garamond", Georgia, serif;
    color: var(--ink);
    position: relative;
  }
  .card {
    position: absolute;
    top: 232px;
    width: 420px;
    height: 735px;
    box-shadow: 0 6px 18px rgba(0,0,0,0.12);
    overflow: hidden;
  }
  /* Back card */
  .card-back { left: 150px; background: var(--charcoal); }
  .card-back .portrait {
    height: 268px;
    background: linear-gradient(180deg, var(--photo-light) 0%, var(--photo-mid) 100%);
  }
  .card-back .brand {
    position: absolute;
    top: 400px; left: 0; right: 0;
    display: flex; flex-direction: column; align-items: center; gap: 18px;
  }
  .brand-square {
    width: 46px; height: 46px;
    background: var(--silver);
  }
  .brand-name {
    color: var(--silver);
    font-size: 30px; font-weight: 600;
    letter-spacing: 0.12em;
    text-transform: uppercase;
  }
  .card-back .address {
    position: absolute;
    bottom: 34px; left: 0; right: 0;
    text-align: center;
    color: var(--silver);
    font-size: 26px; line-height: 1.3;
    letter-spacing: 0.02em;
  }
  /* Front card */
  .card-front {
    left: 630px;
    background: var(--paper);
    padding: 30px;
  }
  .card-front .face {
    position: relative;
    width: 100%; height: 100%;
    background: var(--stone);
  }
  .front-brand {
    position: absolute;
    top: 48px; right: 30px;
    display: flex; align-items: center; gap: 12px;
  }
  .front-brand .brand-square { width: 26px; height: 26px; background: var(--charcoal); }
  .front-brand .brand-name { color: var(--charcoal); font-size: 24px; font-weight: 700; letter-spacing: 0.08em; }
  .agent {
    position: absolute;
    top: 210px; right: 36px;
    width: 250px;
  }
  .agent-name {
    font-size: 34px; font-weight: 500;
    font-variant: small-caps;
    letter-spacing: 0.03em;
  }
  .agent-license {
    font-size: 22px; margin-top: 4px; color: #555;
  }
  .agent-rule {
    margin-top: 22px;
    width: 200px; height: 2px;
    background: var(--ink);
  }
  .contact {
    position: absolute;
    left: 0; bottom: 120px;
    display: flex; align-items: stretch; gap: 16px;
  }
  .contact-keys {
    background: var(--charcoal);
    color: var(--stone);
    width: 44px;
    display: flex; flex-direction: column; justify-content: space-around; align-items: center;
    font-size: 26px; font-weight: 600;
    padding: 4px 0;
  }
  .contact-values { font-size: 30px; line-height: 1.35; font-weight: 500; }
  .website {
    position: absolute;
    left: 20px; bottom: 50px;
    font-size: 25px; font-weight: 500;
  }
</style>
</head>
<body>
  <section class="card card-back">
    <div class="portrait" role="img" aria-label="Portrait photograph of the two agents, Lena and Hank Delcourt"></div>
    <div class="brand">
      <div class="brand-square"></div>
      <div class="brand-name">Delcourt Realty</div>
    </div>
    <p class="address">287 Pohaku Cir. ,<br>Wailea HI 96753</p>
  </section>

  <section class="card card-front">
    <div class="face">
      <div class="front-brand">
        <div class="brand-square"></div>
        <div class="brand-name">DELCOURT REALTY</div>
      </div>
      <div class="agent">
        <h1 class="agent-name">Lena Delcourt</h1>
        <p class="agent-license">R(S) LIC.# 41972</p>
        <div class="agent-rule"></div>
      </div>
      <div class="contact">
        <div class="contact-keys"><span>C</span><span>E</span></div>
        <div class="contact-values">
          <p>555.246.1938</p>
          <p>Lena@Delcourt.example</p>
        </div>
      </div>
      <p class="website">www.IsleFreshHomes.example</p>
    </div>
  </section>
</body>
</html>
```